Criação de Folder para Cascata & Horizonte
" Focada em preservar a vida e o meio ambiente “Gerenciamento de Resíduos da construção civil e demolição", atuando como parceiro da sociedade e das instituições públicas que necessitam dar a estes resíduos a destinação correta sem agredir o meio ambiente. Transforma os resíduos da construção civil em agregados reciclados e reutilizados. Uma das atividades que mais contribui com impactos no meio ambiente é a Construção Civil. Esses impactos ocorrem na fase de implantação da obra, execução dos serviços, confecção de artefatos, limpeza da obra, entre outros. Além disso, são gerados resíduos em toda a vida útil da construção: execução, manutenção, reforma, desocupação e demolição. Vale ressaltar que os resíduos de construção civil constituem a maior parte dos resíduos sólidos urbanos, mas, com a progressiva implantação de políticas de gestão de resíduos e a educação técnica para o uso racional de materiais e recursos em obras, a situação deve mudar. "

```html
<!DOCTYPE html>
<html lang="pt-BR">
<head>
<meta charset="UTF-8">
<title>Folder Cascata &amp; Horizonte</title>
<link href="https://fonts.googleapis.com/css2?family=Open+Sans:wght@400;600;700;800&display=swap" rel="stylesheet">
<style>
  :root{
    --green:#1f9a3e;
    --green-deep:#137a2c;
    --dark:#262a2b;
    --ink:#4a4f52;
    --paper:#ffffff;
    --stage:#e9ece8;
  }
  *{box-sizing:border-box;margin:0;padding:0}
  html,body{width:1200px;height:1200px;overflow:hidden;background:var(--stage);font-family:"Open Sans",sans-serif;color:var(--ink)}
  .folder{position:absolute;left:45px;top:160px;width:1110px;height:880px;display:flex;box-shadow:0 10px 30px rgba(0,0,0,.18)}
  .panel{position:relative;width:370px;height:880px;background:var(--paper);overflow:hidden}
  .panel + .panel{border-left:1px solid #e3e3e3}
  .panel svg.shapes{position:absolute;inset:0;width:370px;height:880px}
  .block{position:absolute}
  .title{color:var(--green);font-weight:800;font-size:19px;letter-spacing:.5px;text-transform:uppercase;margin-bottom:8px}
  .body-text{font-size:13.5px;line-height:1.45;color:var(--ink)}
  .ideals-label{color:#fff;font-weight:800;font-size:20px;letter-spacing:.5px}

  .contact-heading{left:30px;right:30px;top:40px;text-align:center;color:var(--green);font-weight:800;font-size:21px;line-height:1.25}
  .contact-intro{left:40px;right:40px;top:140px;text-align:center;font-size:14px;line-height:1.5}
  .phone{left:0;right:0;top:238px;display:flex;justify-content:center;align-items:center;gap:10px;font-weight:800;font-size:30px;color:var(--dark)}
  .address{left:30px;right:30px;top:290px;text-align:center;font-weight:700;font-size:13.5px;line-height:1.35;color:var(--dark)}
  .social-title{left:0;right:0;top:392px;text-align:center;color:var(--dark);font-weight:800;font-size:15px;letter-spacing:.5px}
  .social-list{left:40px;right:30px;top:430px;display:grid;grid-template-columns:1fr 1fr;row-gap:16px;column-gap:10px;list-style:none}
  .social-list li{display:flex;align-items:center;gap:10px;font-weight:700;font-size:14px;color:var(--dark)}
  .dot{width:22px;height:22px;border-radius:50%;background:var(--green);flex:none}
  .website{left:0;right:0;top:548px;text-align:center;font-weight:600;font-size:12px;letter-spacing:3.5px;color:var(--dark);white-space:nowrap}

  .cover-claim{left:26px;top:420px;width:210px;color:#fff;font-weight:700;font-size:19px;line-height:1.3;text-transform:uppercase}
  .brand{left:0;right:0;top:770px;display:flex;justify-content:center;align-items:center;gap:12px}
  .brand-mark{width:26px;height:26px;background:var(--green)}
  .brand-name{color:var(--green);font-weight:800;font-size:24px}
</style>
</head>
<body>
<main class="folder">

  <section class="panel panel-values">
    <svg class="shapes" viewBox="0 0 370 880">
      <polygon points="0,0 70,0 0,55" fill="var(--dark)"/>
      <polygon points="0,195 195,120 195,440 0,380" fill="var(--green)"/>
      <polygon points="0,650 370,730 370,880 0,880" fill="#7d8f9e" role="img" aria-label="Foto de operário da construção civil com capacete amarelo"/>
      <polygon points="0,635 110,675 0,675" fill="var(--green-deep)"/>
    </svg>
    <div class="block ideals-label" style="left:26px;top:268px">IDEAIS</div>
    <div class="block" style="left:210px;top:100px;width:148px">
      <h3 class="title">Meta</h3>
      <p class="body-text">Nossa meta é realizar a execução de nossas atividades com total segurança para todos os envolvidos, sempre zelando pela integridade física de nosso bem maior que são os nossos colaboradores.</p>
    </div>
    <div class="block" style="left:22px;top:465px;width:170px">
      <h3 class="title">Visão</h3>
      <p class="body-text">Crescer com sustentabilidade, apresentando sempre soluções inteligentes alinhadas às melhores práticas utilizadas no mercado.</p>
    </div>
    <div class="block" style="left:210px;top:465px;width:150px">
      <h3 class="title">Valores</h3>
      <p class="body-text">Honestidade – Ética – Comprometimento – Valorização profissional – Responsabilidade social – Preocupação constante com o meio ambiente – Realização de trabalho seguro.</p>
    </div>
  </section>

  <section class="panel panel-contact">
    <svg class="shapes" viewBox="0 0 370 880">
      <polygon points="0,650 370,580 370,880 0,880" fill="#e8d9a8" role="img" aria-label="Mapa da cidade com marcador de localização"/>
      <polygon points="0,650 90,633 0,690" fill="var(--green)"/>
    </svg>
    <h2 class="block contact-heading">ENTRE EM CONTATO,<br>ESTAMOS PRONTOS<br>PARA ATENDÊ-LO.</h2>
    <p class="block contact-intro">Entre em contato por um dos meios de comunicação abaixo e solicite seu orçamento sem compromisso.</p>
    <div class="block phone">
      <svg width="26" height="26" viewBox="0 0 26 26" aria-hidden="true">
        <circle cx="13" cy="13" r="13" fill="var(--green)"/>
        <path d="M9 7.5c.6-.4 1.3-.2 1.6.4l1 2c.3.5.1 1.1-.3 1.4l-.8.6c.6 1.5 1.8 2.7 3.3 3.3l.6-.8c.3-.4.9-.6 1.4-.3l2 1c.6.3.8 1 .4 1.6l-.7 1c-.5.7-1.4 1-2.2.7C11.8 17.2 8.8 14.2 7.6 10.7c-.3-.8 0-1.7.7-2.2z" fill="#fff"/>
      </svg>
      <span>(00) 0000-0000</span>
    </div>
    <p class="block address">Rua Nome da Rua, 000, Nome do Bairro,<br>Nome da Cidade - UF / CEP 00.000-000</p>
    <h3 class="block social-title">REDES SOCIAIS</h3>
    <ul class="block social-list">
      <li><span class="dot"></span>Mural</li>
      <li><span class="dot"></span>Galeria</li>
      <li><span class="dot"></span>Recados</li>
      <li><span class="dot"></span>Email</li>
    </ul>
    <p class="block website">www.cascatahorizonte.com.br</p>
  </section>

  <section class="panel panel-cover">
    <svg class="shapes" viewBox="0 0 370 880">
      <rect width="370" height="880" fill="var(--dark)"/>
      <polygon points="0,0 370,0 370,280 0,390" fill="#4f6b3a" role="img" aria-label="Foto de árvore crescendo dentro de uma lâmpada sobre a terra"/>
      <polygon points="0,390 370,280 370,560 0,690" fill="var(--green)"/>
      <polygon points="250,315 370,280 370,600 250,640" fill="#3f8f5a" role="img" aria-label="Foto de globo terrestre verde entre folhagens"/>
      <polygon points="0,690 250,602 250,640 0,730" fill="#1a1d1e"/>
      <polygon points="0,830 120,880 0,880" fill="#8a8f90"/>
    </svg>
    <h1 class="block cover-claim">Beneficiamento de resíduos da construção civil e demolição</h1>
    <div class="block brand">
      <span class="brand-mark"></span>
      <span class="brand-name">Cascata &amp; Horizonte</span>
    </div>
  </section>

</main>
</body>
</html>
```